Обновить дизайн коммерческого предложения
Где будет использоваться презентация?
высылаться клиентам
Стоит задача обновить и осовременить дизайн компании (кп, счета, договоры, сайты и т.д.) и сейчас через конкурс ищем дизайнера, который нам поможет.
В качестве первой работы в рамках конкурса необходимо разработать современный дизайн для КП по автовесам.
Технические требования:
1. Логотип, фирменные цвета (RGB: зеленый 0/140/86 и фиолетовый 65/73/129) и шрифт Lato должны остаться прежними.
3. На основе КП по автовесам будет создаваться шаблон для Битрикса, из которого будут формироваться КП для ряда товаров. Поэтому элементы КП (УТП, выгоды, комплектующие, фотографии товара, условия работы) должны быть легко заменяемыми в общем дизайне.
4. Дизайн нужен в пдф и cdr форматах.
КП для которого нужно разработать дизайн
https://fivortel.ru/d/4qLpRw8tNbKzYx

```html
<!DOCTYPE html>
<html lang="ru">
<head>
<meta charset="utf-8">
<title>Коммерческое предложение — автовесы</title>
<link rel="stylesheet" href="https://fonts.googleapis.com/css2?family=Jost:wght@500;600;700&display=swap">
<style>
  :root {
    --bg: #e4e4e4;
    --teal: #2fae9f;
    --green: #008c56;
    --purple: #414981;
    --ink: #111111;
    --panel: #0c0c0e;
    --paper: #ffffff;
    --mist-top: #f1f1f1;
    --mist-bottom: #d9d9d9;
  }
  * { box-sizing: border-box; margin: 0; padding: 0; }
  html, body { width: 1200px; height: 1108px; overflow: hidden; background: var(--bg); }
  body { font-family: "Jost", sans-serif; position: relative; }

  .cover {
    position: absolute; left: 220px; top: 16px;
    width: 760px; height: 1076px;
    background: linear-gradient(180deg, var(--mist-top) 0%, var(--mist-bottom) 100%);
    overflow: hidden;
    box-shadow: 0 6px 24px rgba(0,0,0,.18);
  }
  .cover__header {
    position: absolute; left: 0; top: 0; width: 100%; height: 215px;
    background: var(--paper);
  }
  .cover__tab {
    position: absolute; right: 0; top: 0; width: 150px; height: 46px;
    background: var(--teal);
  }
  .brand {
    position: absolute; left: 40px; top: 122px;
    display: flex; align-items: center; gap: 10px;
  }
  .brand__mark { width: 22px; height: 22px; background: var(--purple); }
  .brand__name {
    font-weight: 700; font-size: 24px; line-height: 1; color: var(--green); letter-spacing: .3px;
  }
  .cover__title {
    position: absolute; left: 290px; top: 78px;
    font-weight: 600; font-size: 44px; line-height: 1.12;
    color: var(--ink); text-transform: uppercase; letter-spacing: 1px;
  }
  .cover__block {
    position: absolute; left: 0; top: 215px; width: 275px; height: 245px;
    background: var(--teal);
  }
  .cover__panel {
    position: absolute; left: 260px; top: 290px; right: 0; bottom: 0;
    background: var(--panel);
  }
  .cover__subtitle {
    position: absolute; left: 260px; right: 0; top: 322px;
    text-align: center; color: #fff; font-weight: 600;
    font-size: 19px; line-height: 1.4;
  }
  .product-visual {
    position: absolute; left: 100px; top: 540px; width: 580px; height: 250px;
    background: radial-gradient(ellipse at center, #c9cbcd 0%, #a8abad 45%, rgba(120,124,128,0) 75%);
  }
  .doc-ref {
    position: absolute; right: 40px; top: 890px;
    text-align: right; color: #fff; font-weight: 600; font-size: 14px; line-height: 1.35;
  }
  .rule { position: absolute; height: 3px; background: #fff; }
  .rule--short { left: 380px; width: 170px; top: 924px; }
  .rule--long { left: 360px; width: 360px; top: 950px; }
  .contractor {
    position: absolute; left: 360px; top: 978px;
    color: var(--teal); font-weight: 600; font-size: 16px; line-height: 1.45;
  }
  .client {
    position: absolute; left: 0; bottom: 0; width: 330px; height: 110px;
    background: var(--paper);
  }
  .client__bar { position: absolute; left: 0; top: 0; width: 24px; height: 100%; background: var(--panel); }
  .client__text {
    position: absolute; left: 44px; top: 34px;
    color: var(--ink); font-weight: 600; font-size: 14px; line-height: 1.45;
  }
</style>
</head>
<body>
  <main class="cover">
    <section class="cover__header">
      <div class="cover__tab"></div>
      <div class="brand">
        <span class="brand__mark"></span>
        <span class="brand__name">ВЕСОТЕХПРОМ</span>
      </div>
      <h1 class="cover__title">Коммерческое<br>предложение</h1>
    </section>

    <div class="cover__block"></div>
    <div class="cover__panel"></div>

    <p class="cover__subtitle">Автовесы с усиленным конструктивом,<br>тензодатчиками KRAVEN и АСУ ТП<br>с полной автоматизацией взвешивания</p>

    <div class="product-visual" role="img" aria-label="Изображение автомобильных весов с платформами, пандусами и жёлтыми отбойниками"></div>

    <p class="doc-ref">Документ №182/16<br>от 05 октября 2016 г.</p>
    <div class="rule rule--short"></div>
    <div class="rule rule--long"></div>

    <p class="contractor">Исполнитель: ООО «ВТП Инжиниринг»<br>Нуриев Р.К., т. 8 (900) 000-12-34</p>

    <section class="client">
      <div class="client__bar"></div>
      <p class="client__text">Заказчик: ООО «Монолит-Строй»<br>Сабирова Л.Р., т. 8 (900) 000-12-34</p>
    </section>
  </main>
</body>
</html>
```